Cedar Ridge Paving. Chip Seal Done Right

I need my card to have all my basic information on it. Keep it simple. Include web site, phone number and email address. Include phrase Chip Seal Done Right or Cedar Ridge’s Top Paving Company. Keep card simple. Include color and logo. Put all contact info on card. Make card simple and not complicated.
Updates

Here is infuriation yo out in business card

Mark T. Delgado
512.408.7316 cell phone
Markdelgado7@mailbrook.net
www.cedarridgepaving.net

Target Market(s)

Hill Country Texas USA

Industry/Entity Type

Road chip seal

Contact Information for Business Card

We chip seal roads for ranches and property owners

Font styles to use
Serif
Sans Serif
Decorative
Script

Colors
0054AA
0677BA
7BADD7
CADEEF
E8F1F8
EB3D1F
EC4F4E
F09395
F8D3D4
FCEDEE

Requirements
Must have
• Keep it simply
Nice to have
• Logo and all basic info

```html
<!DOCTYPE html>
<html lang="en">
<head>
<meta charset="utf-8">
<title>Cedar Ridge Paving — Business Card</title>
<link href="https://fonts.googleapis.com/css2?family=Crimson+Text:wght@400;600&family=Lato:wght@400;700;900&display=swap" rel="stylesheet">
<style>
  :root {
    --bg: #e4e4e4;
    --paper: #ffffff;
    --red: #ac1f2d;
    --navy: #151e4d;
    --white: #ffffff;
  }
  * { box-sizing: border-box; margin: 0; padding: 0; }
  html, body { width: 1047px; height: 1200px; overflow: hidden; }
  body { background: var(--bg); position: relative; font-family: "Lato", sans-serif; }

  .card {
    position: absolute; left: 160px; width: 741px; height: 424px;
    background: var(--paper); overflow: hidden;
    box-shadow: 0 2px 4px rgba(0,0,0,0.18);
  }
  .card--front { top: 120px; }
  .card--back { top: 634px; }

  .front-art { position: absolute; inset: 0; width: 100%; height: 100%; }

  .front-brand {
    position: absolute; left: 60px; top: 170px; width: 240px;
    display: flex; align-items: center; gap: 12px;
  }
  .front-brand__dot { width: 26px; height: 26px; border-radius: 50%; background: var(--navy); flex: none; }
  .front-brand__name {
    font-family: "Lato", sans-serif; font-weight: 900; font-size: 22px;
    line-height: 1.1; color: var(--navy); text-transform: uppercase;
  }

  .contact { position: absolute; right: 47px; top: 73px; text-align: right; color: var(--white); font-family: "Crimson Text", serif; }
  .contact__name { font-weight: 600; font-size: 26px; letter-spacing: 0.5px; text-transform: uppercase; line-height: 1; }
  .contact__title { font-size: 18px; line-height: 1; margin-top: 8px; }

  .contact__list { position: absolute; right: 47px; top: 143px; list-style: none; color: var(--white); font-family: "Crimson Text", serif; font-size: 16.5px; letter-spacing: 0.4px; }
  .contact__item { display: flex; justify-content: flex-end; align-items: flex-start; gap: 14px; text-align: right; line-height: 22.5px; }
  .contact__item + .contact__item { margin-top: 3px; }
  .contact__item--gap { margin-top: 13px !important; }
  .contact__icon { width: 13px; height: 13px; flex: none; margin-top: 5px; fill: var(--white); }

  .back-brand { position: absolute; left: 0; right: 0; top: 100px; display: flex; flex-direction: column; align-items: center; }
  .back-brand__inner { display: inline-flex; flex-direction: column; align-items: flex-end; }
  .back-brand__name {
    font-family: "Lato", sans-serif; font-weight: 900; font-size: 46px;
    line-height: 1.1; color: var(--navy); text-transform: uppercase; letter-spacing: 0.5px; text-align: right;
  }
  .back-brand__years { display: flex; align-items: center; gap: 10px; margin-top: 10px; color: var(--red); font-size: 15px; letter-spacing: 1px; }
  .back-brand__rule { width: 130px; height: 2px; background: var(--red); }

  .tagline { position: absolute; left: 0; right: 0; top: 356px; display: flex; align-items: center; }
  .tagline__line { flex: 1; height: 2px; }
  .tagline__line--navy { background: var(--navy); }
  .tagline__line--red { background: var(--red); }
  .tagline__text { padding: 0 6px 0 8px; font-size: 26px; letter-spacing: 1px; color: var(--navy); white-space: nowrap; }
  .tagline__text strong { color: var(--red); font-weight: 900; }
</style>
</head>
<body>

<section class="card card--front">
  <svg class="front-art" viewBox="0 0 768 440" preserveAspectRatio="none" aria-hidden="true">
    <rect width="768" height="440" fill="var(--red)"/>
    <path d="M0 0 H312 C440 80 470 300 318 440 H0 Z" fill="var(--paper)"/>
    <path d="M365 62 C440 160 440 330 262 440 L300 440 C455 330 448 150 365 62 Z" fill="var(--navy)"/>
  </svg>

  <div class="front-brand">
    <span class="front-brand__dot"></span>
    <span class="front-brand__name">Cedar Ridge Paving</span>
  </div>

  <div class="contact">
    <p class="contact__name">Mark T. Delgado</p>
    <p class="contact__title">Founder &amp; CEO</p>
  </div>

  <ul class="contact__list">
    <li class="contact__item">
      <span>418 Ranch Road 12<br>Wimberley, TX 78676<br>United States</span>
      <svg class="contact__icon" viewBox="0 0 16 16"><path d="M8 0a5.5 5.5 0 0 0-5.5 5.5C2.5 9.6 8 16 8 16s5.5-6.4 5.5-10.5A5.5 5.5 0 0 0 8 0zm0 8a2.5 2.5 0 1 1 0-5 2.5 2.5 0 0 1 0 5z"/></svg>
    </li>
    <li class="contact__item contact__item--gap">
      <span>512.408.7316</span>
      <svg class="contact__icon" viewBox="0 0 16 16"><path d="M3.6 0.8l2.2 2.6c.4.5.3 1.1-.1 1.5L4.6 6c.9 2.2 3.1 4.4 5.4 5.4l1.1-1.1c.4-.4 1-.5 1.5-.1l2.6 2.2c.5.4.5 1.1.1 1.6l-1.3 1.3C11.3 17 -1 4.7 0.8 2l1.3-1.3c.5-.4 1.1-.4 1.5.1z"/></svg>
    </li>
    <li class="contact__item">
      <span>512.408.7316</span>
      <svg class="contact__icon" viewBox="0 0 16 16"><path d="M4 0h8a1 1 0 0 1 1 1v14a1 1 0 0 1-1 1H4a1 1 0 0 1-1-1V1a1 1 0 0 1 1-1zm.6 1.6v10.6h6.8V1.6zM8 13.2a.9.9 0 1 0 0 1.8.9.9 0 0 0 0-1.8z"/></svg>
    </li>
    <li class="contact__item">
      <span>512.408.7316</span>
      <svg class="contact__icon" viewBox="0 0 16 16"><path d="M4 0h8v4H4zM1 5h14a1 1 0 0 1 1 1v6h-3v4H3v-4H0V6a1 1 0 0 1 1-1zm3.5 5.5v4h7v-4z"/></svg>
    </li>
    <li class="contact__item">
      <span>Markdelgado7@mailbrook.net</span>
      <svg class="contact__icon" viewBox="0 0 16 16"><path d="M0 3h16v1.2L8 9 0 4.2zm0 2.6l8 4.8 8-4.8V13H0z"/></svg>
    </li>
    <li class="contact__item">
      <span>www.cedarridgepaving.net</span>
      <svg class="contact__icon" viewBox="0 0 16 16"><path d="M8 0a8 8 0 1 0 0 16A8 8 0 0 0 8 0zm-1 2.2v2.3L4.6 6.2 3 5.3A6 6 0 0 1 7 2.2zM8.5 14c-.8-1-1.6-2.2-1.6-3.4l1.8-1.4 2.6.7.6 2.2A6 6 0 0 1 8.5 14zM12 5.5l-2.2.5L9 3.8l.4-1.4A6 6 0 0 1 12 5.5z"/></svg>
    </li>
  </ul>
</section>

<section class="card card--back">
  <div class="back-brand">
    <div class="back-brand__inner">
      <p class="back-brand__name">Cedar Ridge<br>Paving</p>
      <p class="back-brand__years"><span class="back-brand__rule"></span>OVER 40 YEARS</p>
    </div>
  </div>

  <div class="tagline">
    <span class="tagline__line tagline__line--navy"></span>
    <p class="tagline__text">CHIP SEAL <strong>DONE RIGHT</strong></p>
    <span class="tagline__line tagline__line--red"></span>
  </div>
</section>

</body>
</html>
```